Newsletter-Design für Garten-Samen Shop
Zielgruppe
Online Shop für Obst-, Gemüse-, Kräuter- und Pflanzensamen
Aufgabenstellung
www.beetfreunde-portal.example ist die Seite mit den Produkten. Als Tipp sollte das Jiaogulan genannt werden da dieses Produkt sich am meisten verkauft.

```html
<!DOCTYPE html>
<html lang="de">
<head>
<meta charset="utf-8">
<title>Newsletter – Gartensamen Shop</title>
<link rel="stylesheet" href="https://fonts.googleapis.com/css2?family=Open+Sans:wght@300;400;600&display=swap">
<style>
  :root {
    --green: #8fc590;
    --orange: #ee9769;
    --teal: #5bb3aa;
    --white: #ffffff;
    --paper: #ffffff;
  }
  * { margin: 0; padding: 0; box-sizing: border-box; }
  html, body { width: 1200px; height: 535px; overflow: hidden; background: var(--paper); }
  body { position: relative; font-family: "Open Sans", sans-serif; color: var(--white); }

  .flyer { position: absolute; top: 0; width: 376px; height: 531px; overflow: hidden; }
  .flyer--green { left: 0; }
  .flyer--orange { left: 411px; background: var(--orange); }
  .flyer--teal { left: 824px; background: var(--teal); }

  .photo { position: absolute; }
  .abs { position: absolute; }

  .headline {
    position: absolute; display: flex; align-items: center; justify-content: center;
    text-align: center; font-size: 19px; line-height: 23px; font-weight: 400; color: var(--white);
  }
  .tip-photo {
    position: absolute; border-radius: 50%; border: 2px solid var(--white);
    background: radial-gradient(circle at 55% 45%, #9ccf74 0%, #5f9a45 45%, #3d6e32 100%);
  }
  .tip-label { position: absolute; font-size: 12px; font-weight: 300; white-space: nowrap; }
  .tip-name { position: absolute; font-size: 12.5px; font-weight: 300; white-space: nowrap; }
  .tip-sub { position: absolute; font-size: 6.5px; font-weight: 300; white-space: nowrap; }
  .tip-text { position: absolute; font-size: 6.3px; line-height: 9px; font-weight: 300; }
  .shop-url { position: absolute; font-size: 12px; font-weight: 600; white-space: nowrap; }
  .shop-url--compact { font-size: 10.5px; letter-spacing: -0.1px; }
  .shop-claim { position: absolute; font-size: 6.3px; line-height: 9px; font-weight: 300; }
</style>
</head>
<body>

<section class="flyer flyer--green">
  <div class="photo" role="img" aria-label="Foto von Äpfeln, Karotten, Bananen, Brokkoli und Salat"
       style="inset:0; background: linear-gradient(160deg, #d9e4b8 0%, #9bbf6a 25%, #e07a3a 50%, #b8402e 70%, #8a8e3c 100%);"></div>
  <svg class="abs" style="left:0;top:0" width="376" height="531" viewBox="0 0 376 531">
    <path d="M0 360 C 40 290, 120 262, 210 262 C 300 262, 350 300, 376 320 L376 531 L0 531 Z" fill="var(--green)"/>
    <rect x="55.5" y="24.5" width="267" height="477" fill="none" stroke="var(--white)" stroke-width="1.5"/>
  </svg>
  <div class="headline" style="left:21px;top:65px;width:334px;height:77px;background:var(--green);border:2px solid var(--white);">
    Das beste Obst und Gemüse<br>kommt aus dem eigenen Garten
  </div>
  <div class="tip-photo" role="img" aria-label="Foto einer Jiaogulan-Pflanze" style="left:140px;top:215px;width:96px;height:96px;"></div>
  <div class="tip-label" style="left:186px;top:300px;transform:rotate(-25deg);">Unser Tipp!</div>
  <div class="tip-name" style="left:66px;top:314px;">Jiaogulan</div>
  <div class="tip-sub" style="left:68px;top:331px;">- Das Kraut der Unsterblichkeit</div>
  <div class="tip-text" style="left:68px;top:349px;width:160px;">Das Superfood verbessert die Nähr-<br>stoff-Versorgung aller Organe,  sowie die<br>Herzleistung und die Blutzirkulation.</div>
  <div class="shop-url" style="left:0;width:376px;text-align:center;top:433px;">beetfreunde-portal.example</div>
  <div class="shop-claim" style="left:0;width:376px;text-align:center;top:463px;">Ihr Onlineshop für Obst-,<br>Gemüse-, Kräuter- und<br>Pflanzensamen</div>
</section>

<section class="flyer flyer--orange">
  <div class="photo" role="img" aria-label="Foto von Gurke, Apfelspalten und Karotten auf Holzbrett"
       style="left:0;top:0;width:187px;height:531px;background: linear-gradient(180deg, #5d6b40 0%, #8a9c5e 22%, #c9714a 45%, #e8d6c8 62%, #b5503f 82%, #6a3a2a 100%);"></div>
  <div class="shop-url" style="left:200px;top:35px;">beetfreunde-portal.example</div>
  <div class="shop-claim" style="left:200px;top:64px;">Ihr Onlineshop für Obst-,<br>Gemüse-, Kräuter- und<br>Pflanzensamen</div>
  <div class="headline" style="left:20px;top:158px;width:336px;height:79px;background:var(--orange);border:2px solid var(--white);">
    Das beste Obst und Gemüse<br>kommt aus dem eigenen Garten
  </div>
  <div class="tip-label" style="left:247px;top:352px;transform:rotate(-28deg);">Unser Tipp!</div>
  <div class="tip-photo" role="img" aria-label="Foto einer Jiaogulan-Pflanze" style="left:258px;top:361px;width:94px;height:94px;"></div>
  <div class="tip-name" style="left:200px;top:447px;">Jiaogulan</div>
  <div class="tip-sub" style="left:201px;top:464px;">- Das Kraut der Unsterblichkeit</div>
  <div class="tip-text" style="left:201px;top:482px;width:170px;">Das Superfood verbessert die Nähr-<br>stoff-Versorgung aller Organe,  sowie die<br>Herzleistung und die Blutzirkulation.</div>
</section>

<section class="flyer flyer--teal">
  <div class="photo" role="img" aria-label="Foto von Tomaten, Radieschen, Salat, Gurke und Frühlingszwiebeln"
       style="left:0;top:0;width:376px;height:340px;background: linear-gradient(170deg, #b9bbbd 0%, #a7a9ab 18%, #c9363a 30%, #7fb34a 50%, #3d6a2a 75%, #2f4a22 100%);"></div>
  <svg class="abs" style="left:0;top:0" width="376" height="531" viewBox="0 0 376 531">
    <path d="M0 338 C 120 336, 260 300, 376 222 L376 531 L0 531 Z" fill="var(--teal)"/>
    <polyline points="9.5,346 9.5,521.5 366.5,521.5 366.5,346" fill="none" stroke="var(--white)" stroke-width="1.5"/>
  </svg>
  <div class="headline" style="left:21px;top:31px;width:336px;height:80px;background:rgba(150,150,152,0.55);border:2px solid var(--white);">
    Das beste Obst und Gemüse<br>kommt aus dem eigenen Garten
  </div>
  <div class="tip-photo" role="img" aria-label="Foto einer Jiaogulan-Pflanze" style="left:233px;top:256px;width:92px;height:92px;"></div>
  <div class="tip-label" style="left:276px;top:343px;transform:rotate(-28deg);">Unser Tipp!</div>
  <div class="shop-url shop-url--compact" style="left:24px;top:381px;">beetfreunde-portal.example</div>
  <div class="shop-claim" style="left:24px;top:409px;">Ihr Onlineshop für Obst-,<br>Gemüse-, Kräuter- und<br>Pflanzensamen</div>
  <div class="tip-name" style="left:188px;top:379px;">Jiaogulan</div>
  <div class="tip-sub" style="left:189px;top:396px;">- Das Kraut der Unsterblichkeit</div>
  <div class="tip-text" style="left:189px;top:413px;width:170px;">Das Superfood verbessert die Nähr-<br>stoff-Versorgung aller Organe,  sowie die<br>Herzleistung und die Blutzirkulation.</div>
</section>

</body>
</html>
```